Weight Loss Challenge Social Media Graphics

Create 6-7 individual social media graphics (square size) to encourage folks to join our weight loss challenge. For the color scheme of the graphics, use the color palette attached

Note: each graphic can contain any of the stock photography attached or just the single picture of me (brown shirt) but a few should be ONLY the text
For some graphics we can say: JOIN US!
For some graphics, use only TEXT based

Target Market(s)

primarily women who want to get healthy

Industry/Entity Type

health and weight loss

Requirements
Must have
• The largest text should be: Ninety Days Bold

```html
<!DOCTYPE html>
<html lang="en">
<head>
<meta charset="utf-8">
<title>Ninety Days Bold – Social Graphics</title>
<link rel="stylesheet" href="https://fonts.googleapis.com/css2?family=Barlow+Condensed:wght@300;400;600;700&family=Barlow:wght@400;500;600&display=swap">
<style>
:root{
  --cocoa:#36201a;
  --espresso:#2b1812;
  --mocha:#8c6754;
  --taupe:#b8978e;
  --pink:#f8bfcd;
  --mauve:#b9708a;
  --rose:#d7a1b1;
  --sand:#d9c1a6;
  --cream:#ffffff;
}
*{box-sizing:border-box;margin:0;padding:0}
html,body{width:1200px;height:1200px;overflow:hidden;background:var(--cream)}
.board{
  position:absolute;left:47px;top:46px;
  display:grid;grid-template-columns:repeat(3,363px);grid-template-rows:repeat(3,363px);gap:8px 8px;
}
.tile{position:relative;overflow:hidden;display:flex;flex-direction:column;align-items:center;justify-content:center;text-align:center;font-family:"Barlow Condensed",sans-serif}
.photo{position:absolute;inset:0}
.layer{position:relative;display:flex;flex-direction:column;align-items:center}

/* backgrounds */
.bg-cocoa{background:radial-gradient(circle at 100% 0%,#b79389 0%,#6b4c40 30%,var(--cocoa) 60%,var(--espresso) 100%)}
.bg-mocha{background:linear-gradient(160deg,var(--mocha) 0%,#7b5847 55%,var(--cocoa) 100%)}
.photo-founder{background:linear-gradient(115deg,#a8958a 0%,#cdb9a5 40%,#c29a78 70%,#8a6c5b 100%)}
.photo-group-tan{background:linear-gradient(180deg,#a77a58 0%,#c9a58a 45%,#5b463d 100%)}
.photo-group-mint{background:linear-gradient(180deg,#c9d7cf 0%,#d8bdb3 50%,#9b6f7d 100%)}
.photo-hourglass{background:radial-gradient(circle at 50% 40%,#e6d4c0 0%,#d2b79e 55%,#b89987 85%,#a87b86 100%)}
.photo-tape{background:radial-gradient(circle at 20% 30%,#e6bccb 0%,#d4a0b3 50%,#a9707f 85%,#6e4450 100%)}
.photo-cheer{background:linear-gradient(180deg,#f4b7c6 0%,#e9b6be 50%,#f9e6ec 100%)}

/* brand name set as text */
.mark{display:flex;align-items:center;gap:5px;font-weight:600;letter-spacing:.02em;text-transform:uppercase;line-height:1}
.mark .dot{width:.55em;height:.55em;border-radius:50%;background:currentColor;flex:none}
.mark-sm{font-size:17px}
.mark-lg{font-size:42px}

.pink{color:var(--pink)}
.white{color:var(--cream)}
.mauve{color:var(--mauve)}
.brown{color:var(--cocoa)}

.headline{font-weight:700;text-transform:uppercase;line-height:.9;letter-spacing:-.01em}
.sub-light{font-weight:300;letter-spacing:.05em;text-transform:uppercase}
.tagline{font-family:"Barlow",sans-serif;font-size:12.5px;color:var(--cream)}

/* promo box */
.promo{background:var(--rose);border:6px solid var(--cream);padding:7px 10px 14px;color:var(--cream);position:relative}
.promo-title{font-weight:700;font-size:34px;line-height:1}
.promo-sub{font-family:"Barlow",sans-serif;font-weight:600;font-size:11.5px;margin-top:3px}
.badge{background:var(--espresso);color:var(--cream);font-family:"Barlow",sans-serif;font-weight:600;font-size:10px;padding:5px 12px;letter-spacing:.02em;text-transform:uppercase;white-space:nowrap}
.badge sup{font-size:6px}
.promo .badge{position:absolute;left:50%;bottom:-18px;transform:translateX(-50%)}
</style>
</head>
<body>
<main class="board">

  <section class="tile">
    <div class="photo photo-founder" role="img" aria-label="Smiling founder in a tan turtleneck against a light wall"></div>
    <div class="layer white sub-light" style="position:absolute;left:24px;top:38px;font-size:21px;align-items:flex-start;font-weight:400">Ninety Days Bold</div>
    <div class="layer" style="margin-top:50px;opacity:.85">
      <div class="mark mark-lg mauve"><span class="dot"></span>Steady Forty</div>
      <div class="mark mauve" style="font-size:24px;margin-top:4px">Challenge</div>
    </div>
  </section>

  <section class="tile bg-cocoa">
    <div class="layer" style="margin-top:-38px">
      <div class="mark mark-sm" style="color:#d3a9a4"><span class="dot"></span>Steady Forty Challenge</div>
      <div class="headline pink" style="font-size:78px;margin-top:8px">Join Us!</div>
      <div class="sub-light white" style="font-size:31px;line-height:1;margin-top:2px">Ninety Days Bold!</div>
      <div class="tagline" style="margin-top:2px">Lose Up to 20 Pounds in 6 Weeks!</div>
    </div>
  </section>

  <section class="tile">
    <div class="photo photo-group-tan" role="img" aria-label="Four smiling women in sports bras posing together"></div>
    <div class="layer" style="margin-top:-40px">
      <div class="promo">
        <div class="promo-title">Ninety Days Bold!</div>
        <div class="promo-sub">Lose Up to 20 Pounds in 6 Weeks!</div>
        <div class="badge">Begins Monday, Jan 6<sup>TH</sup></div>
      </div>
    </div>
  </section>

  <section class="tile">
    <div class="photo photo-group-mint" role="img" aria-label="Group of laughing women in activewear"></div>
    <div class="layer" style="margin-top:60px">
      <div class="mark white" style="font-size:22px;margin-bottom:14px"><span class="dot"></span>Steady Forty Challenge</div>
      <div class="promo">
        <div class="promo-title">Ninety Days Bold!</div>
        <div class="promo-sub">Lose Up to 20 Pounds in 6 Weeks!</div>
        <div class="badge">Begins Monday, Jan 6<sup>TH</sup></div>
      </div>
    </div>
  </section>

  <section class="tile">
    <div class="photo photo-hourglass" role="img" aria-label="Hourglass with sand running on a beige backdrop"></div>
    <div class="layer" style="flex-direction:row;align-items:baseline;gap:8px">
      <span class="sub-light white" style="font-size:28px;font-weight:400">Ninety Days</span>
      <span class="headline" style="font-size:46px;color:#4a1f1a">Bold</span>
    </div>
  </section>

  <section class="tile">
    <div class="photo photo-tape" role="img" aria-label="Measuring tape curled on a pink surface"></div>
    <div class="layer" style="margin-top:-40px">
      <div class="mark white" style="font-size:20px"><span class="dot"></span>Steady Forty Challenge</div>
      <div class="headline white" style="font-size:40px;text-transform:none;margin-top:8px">20 Pounds - 6 Weeks</div>
      <div class="badge" style="margin-top:8px">Begins Monday, Jan 6<sup>TH</sup></div>
    </div>
  </section>

  <section class="tile bg-mocha">
    <div class="layer">
      <div class="mark pink" style="font-size:21px"><span class="dot"></span>Steady Forty Challenge</div>
      <div class="headline white" style="font-size:56px;margin-top:10px">It’s Worth It!</div>
    </div>
  </section>

  <section class="tile">
    <div class="photo photo-cheer" role="img" aria-label="Smiling friends celebrating with arms raised, pink toned"></div>
    <div class="layer" style="margin-top:40px;opacity:.72">
      <div class="mark mark-lg brown"><span class="dot"></span>Steady Forty</div>
      <div class="mark brown" style="font-size:26px;margin-top:4px">Challenge</div>
    </div>
  </section>

  <section class="tile bg-cocoa">
    <div class="layer" style="margin-top:10px">
      <div class="headline pink" style="font-size:70px;line-height:.92">Take The<br><span style="font-size:86px">Challenge</span></div>
      <div class="sub-light white" style="font-family:'Barlow',sans-serif;font-size:12.5px;margin-top:8px;letter-spacing:.06em">Lose Up to 20 Pounds in 6 Weeks!</div>
    </div>
  </section>

</main>
</body>
</html>
```